Wine Lable

We Are Moralba Ridge Wines and we are designing a new bottle for our top end wine named "The Velvet Harvest" I no exactly how i want the label to look and im searching for a talented designer to out my vision to life.

There will be 3 parts to this design.

Top Cover design with gold text wrapped around saying"The Velvet Harvest" (See Fig 2)

The front label which i want same as attached (See fig 2)

The Rear label
(See Fig 2 for design)
(See Fig 3 for content)

and final bottle design how it will look together
Updates

Come on guys keep the designs coming

Project Deadline Extended
Reason: I have extended my deadline due to the break from work over the Christmas new year period. Extra consideration will be made

Target Market(s)

The High End wine consumers the bottle cost will be $100USD

Font styles to use
Decorative
Script

Requirements
Must have

• Top Cover design with gold text wrapped around saying"The Velvet Harvest" (See Fig 2)
Black Rear Label with information and company name (Layout Fig 2) (Content Fig 3)
Gold and Black theme
The Text "Wine of Australia" somewhere on the bottle

```html
<!DOCTYPE html>
<html lang="en">
<head>
<meta charset="utf-8">
<title>The Velvet Harvest – Wine Labels</title>
<link rel="stylesheet" href="https://fonts.googleapis.com/css2?family=Oranienbaum&family=Pinyon+Script&family=Playfair+Display:wght@400;500&display=swap">
<style>
  :root {
    --canvas: #000000;
    --label-core: #3a3a3a;
    --label-edge: #050505;
    --gold-light: #f6e39a;
    --gold-mid: #d4b153;
    --gold-deep: #9c7a26;
    --gold-caption: #a8923a;
    --gold-text: #e4ca7a;
    --rule: rgba(212, 177, 83, 0.35);
  }
  * { margin: 0; padding: 0; box-sizing: border-box; }
  html, body { width: 1200px; height: 1000px; overflow: hidden; background: var(--canvas); }
  .sheet { position: relative; width: 1200px; height: 1000px; background: var(--canvas); }
  .frames { position: absolute; inset: 0; }

  .caption {
    position: absolute;
    font-family: "Playfair Display", serif;
    font-size: 15px;
    letter-spacing: 1px;
    color: var(--gold-caption);
  }
  .caption--front-1 { left: 82px; top: 50px; }
  .caption--front-2 { left: 82px; top: 535px; }
  .caption--back { left: 652px; width: 468px; top: 26px; text-align: center; }

  .gold-fill {
    background: linear-gradient(180deg, var(--gold-light) 0%, var(--gold-mid) 55%, var(--gold-deep) 100%);
    -webkit-background-clip: text;
    background-clip: text;
    color: transparent;
  }

  .ornament, .emblem, .region-map { position: absolute; }
  .ornament {
    background: radial-gradient(ellipse at center, rgba(180, 145, 60, 0.35) 0%, rgba(180, 145, 60, 0.08) 60%, transparent 75%);
  }
  .emblem {
    border-radius: 40% 45% 50% 35%;
    background: linear-gradient(90deg, var(--gold-deep), var(--gold-light) 45%, var(--gold-mid) 70%, var(--gold-deep));
  }
  .region-map {
    border-radius: 30% 40% 35% 45%;
    background: linear-gradient(90deg, var(--gold-mid), var(--gold-light) 50%, var(--gold-deep));
  }

  .brand-title {
    position: absolute;
    text-align: center;
    white-space: nowrap;
  }
  .brand-title--serif { font-family: "Oranienbaum", serif; }
  .brand-title--script { font-family: "Pinyon Script", cursive; }

  .tagline, .established {
    position: absolute;
    text-align: center;
    color: var(--gold-text);
    font-family: "Playfair Display", serif;
  }

  .tasting-note {
    position: absolute;
    left: 686px; width: 400px; top: 292px;
    font-family: "Oranienbaum", serif;
    font-size: 18px; line-height: 29px;
    color: var(--gold-text);
    text-align: justify;
    text-align-last: center;
  }
  .info-block {
    position: absolute;
    left: 662px; width: 448px;
    font-family: "Oranienbaum", serif;
    font-size: 18px; line-height: 30px;
    color: var(--gold-text);
    text-align: center;
  }
  .producer { top: 503px; }
  .specs { top: 658px; }
</style>
</head>
<body>
<main class="sheet">
  <svg class="frames" width="1200" height="1000" viewBox="0 0 1200 1000" aria-hidden="true">
    <defs>
      <radialGradient id="label-glow" cx="50%" cy="35%" r="60%">
        <stop offset="0%" stop-color="#3a3a3a"/>
        <stop offset="70%" stop-color="#141414"/>
        <stop offset="100%" stop-color="#050505"/>
      </radialGradient>
      <linearGradient id="gold-frame" x1="0" y1="0" x2="1" y2="1">
        <stop offset="0%" stop-color="#f6e39a"/>
        <stop offset="40%" stop-color="#b8902f"/>
        <stop offset="70%" stop-color="#e9cf7a"/>
        <stop offset="100%" stop-color="#8c6a1f"/>
      </linearGradient>
    </defs>

    <!-- front option 1 -->
    <polygon points="82,77 550,77 550,340 316,462 82,340" fill="url(#label-glow)" stroke="url(#gold-frame)" stroke-width="4"/>
    <polygon points="92,87 540,87 540,335 316,450 92,335" fill="none" stroke="url(#gold-frame)" stroke-width="1.6"/>
    <line x1="92" y1="268" x2="540" y2="268" stroke="var(--rule)" stroke-width="1"/>
    <line x1="92" y1="318" x2="540" y2="318" stroke="var(--rule)" stroke-width="1"/>

    <!-- front option 2 -->
    <polygon points="82,562 550,562 550,825 316,945 82,825" fill="url(#label-glow)" stroke="url(#gold-frame)" stroke-width="4"/>
    <polygon points="92,572 540,572 540,820 316,933 92,820" fill="none" stroke="url(#gold-frame)" stroke-width="1.6"/>
    <line x1="92" y1="758" x2="540" y2="758" stroke="var(--rule)" stroke-width="1"/>
    <line x1="92" y1="798" x2="540" y2="798" stroke="var(--rule)" stroke-width="1"/>

    <!-- back label -->
    <polygon points="652,52 1120,52 1120,830 886,948 652,830" fill="url(#label-glow)" stroke="url(#gold-frame)" stroke-width="4"/>
    <polygon points="662,62 1110,62 1110,826 886,937 662,826" fill="none" stroke="url(#gold-frame)" stroke-width="1.6"/>
    <line x1="676" y1="216" x2="1096" y2="216" stroke="var(--rule)" stroke-width="1"/>
    <line x1="676" y1="275" x2="1096" y2="275" stroke="var(--rule)" stroke-width="1"/>
    <line x1="676" y1="488" x2="1096" y2="488" stroke="var(--rule)" stroke-width="1"/>
    <line x1="676" y1="640" x2="1096" y2="640" stroke="var(--rule)" stroke-width="1"/>
  </svg>

  <p class="caption caption--front-1">FRONT OPTION 1</p>
  <p class="caption caption--front-2">FRONT OPTION 2</p>
  <p class="caption caption--back">BACK</p>

  <!-- front option 1 content -->
  <div class="ornament" role="img" aria-label="Gold scroll flourish" style="left:180px;top:118px;width:272px;height:50px;"></div>
  <div class="emblem" role="img" aria-label="Gold grape leaf emblem" style="left:287px;top:182px;width:56px;height:72px;"></div>
  <h2 class="brand-title brand-title--serif gold-fill" style="left:92px;width:448px;top:268px;font-size:44px;line-height:50px;">THE VELVET HARVEST</h2>
  <p class="tagline" style="left:92px;width:448px;top:332px;font-size:16px;letter-spacing:1.5px;">WINE OF AUSTRALIA</p>
  <p class="established" style="left:92px;width:448px;top:358px;font-size:14px;">EST. 2015</p>
  <div class="ornament" role="img" aria-label="Gold scroll flourish" style="left:240px;top:385px;width:152px;height:38px;"></div>

  <!-- front option 2 content -->
  <div class="ornament" role="img" aria-label="Gold scroll flourish" style="left:180px;top:602px;width:272px;height:62px;"></div>
  <div class="emblem" role="img" aria-label="Gold grape leaf emblem" style="left:284px;top:664px;width:62px;height:78px;"></div>
  <h2 class="brand-title brand-title--script gold-fill" style="left:92px;width:448px;top:754px;font-size:40px;line-height:52px;">The Velvet Harvest</h2>
  <p class="tagline" style="left:92px;width:448px;top:812px;font-family:'Pinyon Script',cursive;font-size:24px;">Wine of Australia</p>
  <p class="established" style="left:92px;width:448px;top:848px;font-size:14px;">EST. 2015</p>
  <div class="ornament" role="img" aria-label="Gold scroll flourish" style="left:240px;top:870px;width:152px;height:36px;"></div>

  <!-- back label content -->
  <div class="ornament" role="img" aria-label="Gold scroll flourish" style="left:790px;top:94px;width:192px;height:46px;"></div>
  <div class="emblem" role="img" aria-label="Gold grape leaf emblem" style="left:861px;top:136px;width:52px;height:60px;"></div>
  <h1 class="brand-title brand-title--serif gold-fill" style="left:662px;width:448px;top:218px;font-size:50px;line-height:56px;">THE VELVET HARVEST</h1>
  <p class="tasting-note">Deep, vibrant crimson/garnet colour. Blackcurrant and plum aromas with lifted clove-like spice complemented by toasty oak and a touch of fennel. Intense but balanced juicy red currant and plum characters on the palate with a gentle spice. Generous, soft mouth-filling tannins and balanced acidity.</p>
  <address class="info-block producer" style="font-style:normal;">
    Produced by: Stag Hill Australia<br>
    Shop 4, 212 Upper Ridge Road<br>
    Marlow Vale 5088<br>
    South Australia, Australia
  </address>
  <p class="info-block specs">
    Net Content 750ml<br>
    Alcohol Strength 15.5%<br>
    Approx 9.1 Standard Drinks<br>
    Contains Sulphites
  </p>
  <div class="region-map" role="img" aria-label="Gold map of Australia with South Australia marked" style="left:846px;top:785px;width:88px;height:52px;"></div>
  <div class="ornament" role="img" aria-label="Gold scroll flourish" style="left:812px;top:862px;width:148px;height:38px;"></div>
</main>
</body>
</html>
```